Capital Management company needs a web design

We have a domain name and logo but need hosting and design. Please look at the Must-Haves section.

Target Market(s)

banking industry and investors

Industry/Entity Type

Investment

Coding

Coded - Design and coding required

Number of Pages Required

1 page

Font styles to use
Sans Serif

Requirements
Must have
• Picture(s) of skyscraper skyline (can be of Manhattan, Chicago, or any other major city in the USA).
• Please use the three colors of the logo as a backdrop to part of the webpage(s)
Should not have
• No "what our clients say" section
• No pictures of people

```html
<!DOCTYPE html>
<html lang="en">
<head>
<meta charset="utf-8">
<title>Northbank Capital Management</title>
<link href="https://fonts.googleapis.com/css2?family=Rubik:wght@400;500;700;900&family=Roboto:wght@400;500;700&display=swap" rel="stylesheet">
<style>
:root{
  --blue:#1a73ba;
  --blue-mid:#3f86c2;
  --blue-dark:#155f9c;
  --ink:#222a33;
  --text:#555d66;
  --muted:#8a9099;
  --line:#e4e7eb;
  --soft:#f6f7f8;
  --white:#ffffff;
}
*{box-sizing:border-box;margin:0;padding:0}
html,body{width:1200px;height:3364px;overflow:hidden}
body{font-family:"Roboto",Arial,sans-serif;color:var(--text);background:var(--white);position:relative}
.abs{position:absolute}
a{color:inherit;text-decoration:none}

/* top bar */
.topbar{top:0;left:0;width:1200px;height:29px;background:var(--blue);color:var(--white);font-size:11px}
.topbar .tabs{position:absolute;left:160px;top:0;display:flex;height:29px}
.topbar .tabs span{padding:0 12px;line-height:29px}
.topbar .tabs .active{background:var(--white);color:var(--blue)}
.topbar .util{position:absolute;right:160px;top:0;line-height:29px;display:flex;gap:28px}

/* header */
.header{top:29px;left:0;width:1200px;height:94px;background:var(--white)}
.brand{position:absolute;left:160px;top:28px;display:flex;align-items:center;gap:10px;font-family:"Rubik",sans-serif;font-weight:700;font-size:22px;color:var(--blue)}
.brand .mark{width:14px;height:14px;background:var(--blue)}
.nav{position:absolute;right:160px;top:36px;display:flex;gap:26px;font-size:11px;color:var(--muted);align-items:center}
.nav .active{background:var(--blue);color:var(--white);padding:4px 10px;border-radius:10px;font-weight:500}

/* hero */
.hero{top:123px;left:0;width:1200px;height:449px;background:linear-gradient(180deg,#6f7a86 0%,#4c5663 45%,#2a3340 80%,#1c2530 100%);text-align:center;color:var(--white)}
.hero .kicker{position:absolute;top:165px;width:100%;font-size:15px;font-family:"Rubik",sans-serif;letter-spacing:.3px}
.hero h1{position:absolute;top:186px;width:100%;font-family:"Rubik",sans-serif;font-weight:900;font-size:41px}
.hero .cta{position:absolute;top:256px;left:552px;width:96px;height:24px;border-radius:12px;background:var(--blue);border:1px solid #fff;font-size:9px;font-weight:700;line-height:22px}
.hero .dots{position:absolute;top:390px;left:0;width:100%;display:flex;justify-content:center;gap:16px}
.hero .dots i{width:14px;height:14px;border:2px solid #fff;border-radius:50%}
.hero .dots i:first-child{background:#fff}
.hero .arrow{position:absolute;top:202px;width:22px;height:44px;background:var(--blue);display:flex;align-items:center;justify-content:center}
.hero .arrow.next{right:0;background:#fff}

/* intro */
.intro{top:572px;left:0;width:1200px;height:639px;background:var(--soft)}
.features{position:absolute;top:38px;left:161px;display:flex;gap:14px}
.feature{width:163px;height:164px;background:var(--white);border:1px solid var(--line);text-align:center;color:var(--blue);font-family:"Rubik",sans-serif;font-size:15px;font-weight:500;padding-top:28px}
.feature svg{display:block;margin:0 auto 18px}
.feature.active{background:var(--blue-mid);color:var(--white)}
.section-title{font-family:"Rubik",sans-serif;font-size:28px;color:var(--ink);text-align:center}
.section-title b{color:var(--blue);font-weight:500}
.intro h2{position:absolute;top:258px;width:100%}
.intro .copy{position:absolute;top:322px;left:160px;width:880px;text-align:center;font-size:10.5px;line-height:17px}
.intro .copy p{margin-bottom:10px}

/* services */
.services-card{top:1106px;left:161px;width:878px;height:464px;background:var(--white);border:1px solid var(--line)}
.services-card h2{position:absolute;top:50px;width:100%}
.services{position:absolute;top:120px;left:0;width:100%;display:flex}
.service{flex:1;text-align:center;padding:0 18px;border-right:1px solid var(--line);height:190px}
.service:last-child{border-right:none}
.service h3{font-family:"Rubik",sans-serif;font-weight:500;font-size:16px;color:var(--ink);margin:14px 0 8px}
.service p{font-size:10px;line-height:15px;color:var(--muted)}
.btn-pill{display:inline-block;margin-top:14px;width:84px;height:24px;line-height:22px;border-radius:12px;border:1px solid var(--blue);color:var(--blue);font-size:9px;font-weight:700}
.btn-pill.solid{background:var(--blue);color:#fff}
.services-card .all{position:absolute;top:366px;left:377px;width:124px;margin:0}

/* news */
.news{top:1575px;left:0;width:1200px;height:892px;background:var(--blue-mid)}
.news h2{position:absolute;left:175px;top:50px;font-family:"Rubik",sans-serif;font-weight:500;font-size:28px;color:#fff}
.news h2 span{font-weight:400}
.news .all{position:absolute;right:160px;top:63px;color:#fff;font-size:10px;font-weight:700}
.card{position:absolute;width:276px;height:341px;background:#fff;border-radius:4px;overflow:hidden}
.card .photo{height:144px;margin:8px 8px 0;border-radius:2px}
.card .body{padding:22px 15px}
.card .date{font-size:10px;font-weight:700;color:var(--ink)}
.card h3{font-family:"Rubik",sans-serif;font-weight:500;font-size:14px;color:var(--ink);line-height:18px;margin:14px 0 10px}
.card p{font-size:10.5px;line-height:16px}
.card .more{display:block;margin-top:16px;font-size:10px;font-weight:700;color:var(--blue)}

/* partners */
.partners{top:2467px;left:0;width:1200px;height:220px;background:#fff}
.partners h2{position:absolute;top:52px;width:100%;font-weight:400}
.partner-row{position:absolute;top:128px;left:165px;width:870px;display:flex;justify-content:space-between;align-items:center}
.partner-row i{display:block;height:22px;background:#3c4a5a;border-radius:3px;opacity:.85}

/* newsletter */
.newsletter{top:2687px;left:0;width:1200px;height:258px;background:var(--soft);text-align:center}
.newsletter h2{position:absolute;top:62px;width:100%;font-weight:500;font-size:29px}
.newsletter p{position:absolute;top:112px;width:100%;font-size:13px}
.newsletter .form{position:absolute;top:155px;left:425px;display:flex;gap:10px}
.newsletter .input{width:246px;height:34px;background:#fff;border:1px solid var(--line);border-radius:2px;font-size:10px;color:var(--muted);text-align:left;padding:11px 12px}
.newsletter .go{width:92px;height:34px;border-radius:17px;background:var(--blue);color:#fff;font-size:11px;font-weight:700;line-height:34px}

/* footer */
.footer-top{top:2945px;left:0;width:1200px;height:90px;background:#fff}
.footer-top .brand{top:32px}
.footer-top .call{position:absolute;left:577px;top:36px;font-family:"Rubik",sans-serif;font-weight:500;font-size:21px;color:var(--ink)}
.social{position:absolute;left:840px;top:26px;display:flex;gap:12px}
.social i{width:40px;height:40px;border-radius:50%;border:2px solid var(--blue);display:block}
.social i:first-child{background:var(--blue)}
.footer{top:3035px;left:0;width:1200px;height:262px;background:var(--blue);color:#fff}
.footer .col{position:absolute;top:62px;font-size:11px;line-height:18px}
.footer h4{font-family:"Rubik",sans-serif;font-weight:500;font-size:14px;margin-bottom:12px}
.footer ul{list-style:none}
.footer .about p{width:200px}
.bottom{top:3297px;left:0;width:1200px;height:67px;background:var(--blue-dark);color:#fff;font-size:10px}
.bottom span{position:absolute;left:161px;top:28px}
</style>
</head>
<body>

<div class="abs topbar">
  <div class="tabs"><span>Personal</span><span>Business</span><span class="active">Helps &amp; Tips</span></div>
  <div class="util"><span>Login</span><span>Search</span></div>
</div>

<header class="abs header">
  <div class="brand"><span class="mark"></span>Northbank Capital Management</div>
  <nav class="nav">
    <a class="active">Story</a><a>Our Team</a><a>Services</a><a>News &amp; Insights</a><a>About Us</a><a>Contact</a>
  </nav>
</header>

<section class="abs hero" role="img" aria-label="City skyline of downtown skyscrapers at dusk">
  <div class="kicker">WE PROVIDE BEST CAPITAL MANAGEMENT</div>
  <h1>Nurture the Future with invest</h1>
  <a class="cta">CONTACT US</a>
  <div class="dots"><i></i><i></i><i></i><i></i></div>
  <div class="arrow prev"><svg width="8" height="12" viewBox="0 0 8 12"><path d="M6 1 1 6l5 5" stroke="#fff" stroke-width="2" fill="none"/></svg></div>
  <div class="arrow next"><svg width="8" height="12" viewBox="0 0 8 12"><path d="M2 1l5 5-5 5" stroke="#333" stroke-width="2" fill="none"/></svg></div>
</section>

<section class="abs intro">
  <div class="features">
    <div class="feature active">
      <svg width="44" height="44" viewBox="0 0 44 44" fill="none" stroke="#fff" stroke-width="2"><path d="M22 8a10 10 0 0 0-6 18v5h12v-5a10 10 0 0 0-6-18zM17 35h10M19 39h6M22 1v3M6 16H3M41 16h-3M9 5l2 2M35 5l-2 2"/></svg>
      Explore Our<br>Capabilities</div>
    <div class="feature">
      <svg width="44" height="44" viewBox="0 0 44 44" fill="none" stroke="#1a73ba" stroke-width="2"><ellipse cx="22" cy="25" rx="15" ry="11"/><path d="M12 34v5h5v-3M27 36v3h5v-5M37 23h4v6h-4"/><circle cx="22" cy="8" r="5"/></svg>
      Find a Fund</div>
    <div class="feature">
      <svg width="44" height="44" viewBox="0 0 44 44" fill="none" stroke="#1a73ba" stroke-width="2.5"><rect x="4" y="10" width="36" height="26" rx="2"/><path d="M4 12l18 13 18-13"/></svg>
      Subscribe to<br>Updates</div>
    <div class="feature">
      <svg width="44" height="44" viewBox="0 0 44 44" fill="none" stroke="#1a73ba" stroke-width="2.5"><circle cx="18" cy="18" r="13"/><path d="M28 28l12 12"/></svg>
      Learn about<br>NCM</div>
    <div class="feature">
      <svg width="44" height="44" viewBox="0 0 44 44" fill="none" stroke="#1a73ba" stroke-width="2"><path d="M4 40h36M9 38V28M17 38V22M25 38V16M33 38V10"/><circle cx="9" cy="22" r="3"/><circle cx="17" cy="16" r="3"/><circle cx="25" cy="10" r="3"/><circle cx="33" cy="5" r="3"/></svg>
      Read our<br>latest insights</div>
  </div>
  <h2 class="section-title"><b>Capital</b> and <b>Investment</b> Management</h2>
  <div class="copy">
    <p>Lorem ipsum dolor sit amet, consectetur adipiscing elit, sed do eiusmod tempor incididunt ut labore et dolore magna aliqua. Ut enim ad minim veniam, quis nostrud exercitation ullamco laboris nisi ut aliquip ex ea commodo consequat. Duis aute irure dolor in reprehenderit in voluptate velit esse cillum dolore eu fugiat nulla pariatur. Excepteur sint occaecat cupidatat non proident, sunt in culpa qui officia deserunt mollit anim id est laborum.</p>
    <p>Sed ut perspiciatis unde omnis iste natus error sit voluptatem accusantium doloremque laudantium, totam rem aperiam, eaque ipsa quae ab illo inventore veritatis et quasi architecto beatae vitae dicta sunt explicabo.</p>
    <p>Nemo enim ipsam voluptatem quia voluptas sit aspernatur aut odit aut fugit, sed quia consequuntur magni dolores eos qui ratione voluptatem sequi nesciunt.</p>
  </div>
</section>

<section class="abs services-card">
  <h2 class="section-title">What We <b>Do</b></h2>
  <div class="services">
    <div class="service">
      <svg width="40" height="40" viewBox="0 0 40 40" fill="none" stroke="#1a73ba" stroke-width="2"><rect x="8" y="4" width="24" height="30" rx="2"/><path d="M13 12h14M13 18h14M13 24h8M4 36h32"/></svg>
      <h3>Fixed Income</h3>
      <p>Nemo enim ipsam voluptatem quia voluptas sit aspernatur aut odit aut fugit, sed quia consequuntur</p>
      <a class="btn-pill solid">READ MORE</a>
    </div>
    <div class="service">
      <svg width="40" height="40" viewBox="0 0 40 40" fill="none" stroke="#1a73ba" stroke-width="2"><circle cx="20" cy="14" r="9"/><path d="M4 34c4-6 10-8 16-6l8 2M20 10v8"/></svg>
      <h3>Multi-Assets</h3>
      <p>Nemo enim ipsam voluptatem quia voluptas sit aspernatur aut odit aut fugit, sed quia consequuntur</p>
      <a class="btn-pill">READ MORE</a>
    </div>
    <div class="service">
      <svg width="40" height="40" viewBox="0 0 40 40" fill="none" stroke="#1a73ba" stroke-width="2"><path d="M4 20L20 6l16 14M9 16v18h22V16M17 34v-9h6v9"/></svg>
      <h3>Real Estate</h3>
      <p>Nemo enim ipsam voluptatem quia voluptas sit aspernatur aut odit aut fugit, sed quia consequuntur</p>
      <a class="btn-pill">READ MORE</a>
    </div>
    <div class="service">
      <svg width="40" height="40" viewBox="0 0 40 40" fill="none" stroke="#1a73ba" stroke-width="2"><circle cx="12" cy="10" r="4"/><circle cx="28" cy="10" r="4"/><circle cx="20" cy="22" r="4"/><path d="M6 36v-6h28v6M12 14v6M28 14v6"/></svg>
      <h3>Private Equity</h3>
      <p>Nemo enim ipsam voluptatem quia voluptas sit aspernatur aut odit aut fugit, sed quia consequuntur</p>
      <a class="btn-pill">READ MORE</a>
    </div>
  </div>
  <a class="btn-pill solid all">SEE ALL SERVICES</a>
</section>

<section class="abs news">
  <h2>News <span>&amp;</span> Insights</h2>
  <a class="all">SEE ALL INSIGHTS</a>

  <article class="card" style="left:161px;top:125px">
    <div class="photo" role="img" aria-label="Financial charts on paper and a tablet" style="background:linear-gradient(135deg,#dfe6ec,#9fb4c6)"></div>
    <div class="body"><div class="date">21 AUGUST, 2019</div><h3>Nemo enim ipsam voluptatem quia voluptas sit aspe</h3><p>Lorem ipsum dolor sit amet, consectetur adipiscing elit, sed do eiusmod tempor incididunt ut labore et dolore magna aliqua.</p><a class="more">READ MORE</a></div>
  </article>
  <article class="card" style="left:462px;top:125px">
    <div class="photo" role="img" aria-label="Model house on property documents" style="background:linear-gradient(135deg,#c9ccce,#7d8288)"></div>
    <div class="body"><div class="date">21 AUGUST, 2019</div><h3>Nemo enim ipsam voluptatem quia voluptas sit aspe</h3><p>Lorem ipsum dolor sit amet, consectetur adipiscing elit, sed do eiusmod tempor incididunt ut labore et dolore magna aliqua.</p><a class="more">READ MORE</a></div>
  </article>
  <article class="card" style="left:763px;top:125px">
    <div class="photo" role="img" aria-label="Banknotes, a pen and a cheque on a desk" style="background:linear-gradient(135deg,#eceae6,#b5ada0)"></div>
    <div class="body"><div class="date">21 AUGUST, 2019</div><h3>Nemo enim ipsam voluptatem quia voluptas sit aspe</h3><p>Lorem ipsum dolor sit amet, consectetur adipiscing elit, sed do eiusmod tempor incididunt ut labore et dolore magna aliqua.</p><a class="more">READ MORE</a></div>
  </article>
  <article class="card" style="left:161px;top:491px">
    <div class="photo" role="img" aria-label="Stack of banknotes" style="background:linear-gradient(135deg,#8c8f7a,#3d4136)"></div>
    <div class="body"><div class="date">21 AUGUST, 2019</div><h3>Nemo enim ipsam voluptatem quia voluptas sit aspe</h3><p>Lorem ipsum dolor sit amet, consectetur adipiscing elit, sed do eiusmod tempor incididunt ut labore et dolore magna aliqua.</p><a class="more">READ MORE</a></div>
  </article>
  <article class="card" style="left:462px;top:491px">
    <div class="photo" role="img" aria-label="House keys being handed over" style="background:linear-gradient(135deg,#d4c9bf,#6e5e52)"></div>
    <div class="body"><div class="date">21 AUGUST, 2019</div><h3>Nemo enim ipsam voluptatem quia voluptas sit aspe</h3><p>Lorem ipsum dolor sit amet, consectetur adipiscing elit, sed do eiusmod tempor incididunt ut labore et dolore magna aliqua.</p><a class="more">READ MORE</a></div>
  </article>
  <article class="card" style="left:763px;top:491px">
    <div class="photo" role="img" aria-label="Finance notes and laptop on a wooden desk" style="background:linear-gradient(135deg,#a68a6c,#3f3127)"></div>
    <div class="body"><div class="date">21 AUGUST, 2019</div><h3>Nemo enim ipsam voluptatem quia voluptas sit aspe</h3><p>Lorem ipsum dolor sit amet, consectetur adipiscing elit, sed do eiusmod tempor incididunt ut labore et dolore magna aliqua.</p><a class="more">READ MORE</a></div>
  </article>
</section>

<section class="abs partners">
  <h2 class="section-title">Featured <b>Partners</b></h2>
  <div class="partner-row" aria-label="Partner badges">
    <i style="width:92px"></i><i style="width:84px"></i><i style="width:86px"></i><i style="width:66px;height:30px"></i><i style="width:88px"></i><i style="width:92px"></i>
  </div>
</section>

<section class="abs newsletter">
  <h2 class="section-title">Get More from <b>Northbank Capital Management</b></h2>
  <p>Don't miss important Updates for all the time.</p>
  <div class="form"><div class="input">Enter your email address</div><a class="go">SUBSCRIBE</a></div>
</section>

<div class="abs footer-top">
  <div class="brand"><span class="mark"></span>Northbank Capital Management</div>
  <div class="call">Call Us 555-010-2468</div>
  <div class="social" aria-label="Social links"><i></i><i></i><i></i><i></i></div>
</div>

<footer class="abs footer">
  <div class="col about" style="left:161px"><h4>ABOUT US</h4><p>Lorem ipsum dolor sit amet, consectetur adipiscing elit, sed do eiusmod tempor incididunt ut labore et dolore magna aliqua. Ut enim ad minim veniam, quis nostrud exercitation ullamco laboris, sed do eiusmod tempor incididunt ut labore et dolore magna aliqua.</p></div>
  <div class="col" style="left:446px"><h4>QUICK LINKS</h4><ul><li>Story</li><li>Our Team</li><li>Services</li><li>News &amp; Insights</li><li>About Us</li><li>Contact</li></ul></div>
  <div class="col" style="left:664px"><h4>COMMUNITY</h4><ul><li>Blog</li><li>Customer Stories</li><li>Webinars</li><li>Help &amp; Support</li><li>Resources</li></ul></div>
  <div class="col" style="left:884px"><h4>MEET</h4><ul><li>About</li><li>Meet Our Team</li><li>Careers</li><li>News</li><li>Community</li></ul></div>
</footer>

<div class="abs bottom"><span>© Northbank Capital Management 2019. All rights reserved.</span></div>

</body>
</html>
```